Business Card Design

We like to use greens as you will see in our logo (but not TOO much green). We are a Dental Clinic in a somewhat eccentric community. We do not like the dated sharp designs which we see many dentists use. We're looking for something bright and fresh while still maintaining the integrity of the profession. Elegance is not necessarily what we are going for... we need for the design to be "mature" but also up-lifting.

See our logo.
Updates

Project Deadline Extended
Reason: We have 5 designs which we like. But we'd like to see a few more before committing to a design.

Project Deadline Extended
Reason: We are awaiting revisions to this project. We are still welcoming designs while we wait to see if designers are able to provide to us the revisions we require in order to proceed with a selection.

Target Market(s)

Younger families - ages late 20's to early 40's

Industry/Entity Type

Business

Contact Information for Business Card

Marlow T. Venn DDS 2737 S. Fennimore Ave. Ste. 8 Royal Oak, MI 48059 (248)555-0174 FX (248)555-0189 info@BrightwaveDentalMi.example BrigthwaveDentalMi.example on the back of the card we need an appointment reminder (For____ Date___ Time____) with "If you are unable to keep your appointment, kindly give 48 hours notice" at the bottom. No use of teeth in the design. DOUBLE SIDED DESIGN

Requirements
Should not have
• The use of pictures of teeth

```html
<!DOCTYPE html>
<html lang="en">
<head>
<meta charset="utf-8">
<title>Brightwave Dental Care – Business Card</title>
<link rel="stylesheet" href="https://fonts.googleapis.com/css2?family=Source+Sans+3:wght@400;600&display=swap">
<style>
  :root {
    --page-bg: #e9eaec;
    --card-bg: #e3efc4;
    --ink-green: #2f7a34;
    --text-green: #3b7d3a;
    --rule-green: #8cc26a;
    --circle-a: #cfe2ab;
    --circle-b: #bfd79c;
    --circle-c: #b3cd95;
  }
  * { box-sizing: border-box; margin: 0; padding: 0; }
  html, body {
    width: 1200px; height: 1200px; overflow: hidden;
    background: var(--page-bg);
    font-family: "Source Sans 3", "Segoe UI", sans-serif;
    color: var(--text-green);
  }
  .canvas { position: relative; width: 1200px; height: 1200px; }
  .card {
    position: absolute; left: 260px; width: 680px; height: 390px;
    background: var(--card-bg); overflow: hidden;
  }
  .card--front { top: 160px; }
  .card--back { top: 640px; }
  .card__decor { position: absolute; inset: 0; }

  /* wordmark */
  .wordmark { position: absolute; display: flex; align-items: center; gap: 10px; }
  .wordmark__dot { width: 20px; height: 20px; border-radius: 50%; background: var(--ink-green); flex: none; }
  .wordmark__name { font-weight: 600; color: var(--ink-green); line-height: 1.05; }
  .wordmark__line { display: block; }
  .card--front .wordmark { left: 80px; top: 120px; }
  .card--front .wordmark__name { font-size: 40px; }
  .card--front .wordmark__line--sub { font-size: 24px; margin-top: 4px; }
  .card--back .wordmark { left: 50%; top: 50px; transform: translateX(-50%); white-space: nowrap; }
  .card--back .wordmark__name { font-size: 28px; }

  /* front */
  .dentist { position: absolute; right: 56px; top: 132px; text-align: right; font-size: 30px; line-height: 1.25; }
  .dentist__credential { display: block; font-size: 22px; padding-right: 12px; }
  .rule { position: absolute; background: var(--rule-green); }
  .rule--h { left: 16px; right: 30px; top: 280px; height: 2px; }
  .rule--v { left: 386px; top: 280px; width: 2px; height: 96px; }
  .side-bar { position: absolute; right: 0; top: 280px; width: 30px; height: 110px; background: var(--circle-b); }
  .contacts { position: absolute; left: 24px; top: 292px; list-style: none; font-size: 22px; line-height: 28px; }
  .contacts li { display: flex; align-items: center; gap: 16px; }
  .contacts svg { width: 18px; height: 18px; fill: var(--text-green); flex: none; }
  .address { position: absolute; left: 400px; top: 290px; display: flex; gap: 14px; font-size: 21px; line-height: 28px; font-style: normal; }
  .address svg { width: 28px; height: 26px; fill: var(--ink-green); margin-top: 2px; flex: none; }

  /* back */
  .website { position: absolute; top: 136px; width: 100%; text-align: center; font-size: 24px; }
  .appointment { position: absolute; top: 208px; width: 100%; text-align: center; font-size: 24px; word-spacing: 4px; }
  .blank { display: inline-block; border-bottom: 2px solid var(--text-green); height: 1px; }
  .blank--for { width: 70px; }
  .blank--date { width: 60px; }
  .blank--time { width: 50px; }
  .notice { position: absolute; top: 310px; width: 100%; text-align: center; font-size: 22px; line-height: 28px; }
</style>
</head>
<body>
<main class="canvas">

  <section class="card card--front" aria-label="Card front">
    <svg class="card__decor" viewBox="0 0 680 390" aria-hidden="true">
      <circle cx="650" cy="40" r="90" fill="var(--circle-a)"/>
      <circle cx="620" cy="120" r="100" fill="var(--circle-b)" opacity="0.8"/>
    </svg>
    <div class="side-bar"></div>

    <div class="wordmark">
      <span class="wordmark__dot"></span>
      <span class="wordmark__name"><span class="wordmark__line">Brightwave</span><span class="wordmark__line wordmark__line--sub">Dental Care</span></span>
    </div>

    <p class="dentist">Marlow T. Venn<span class="dentist__credential">DDS 2737 S.</span></p>

    <div class="rule rule--h"></div>
    <div class="rule rule--v"></div>

    <ul class="contacts">
      <li><svg viewBox="0 0 24 24" aria-label="Phone"><path d="M6.6 10.8a15 15 0 0 0 6.6 6.6l2.2-2.2c.3-.3.7-.4 1-.2 1.1.4 2.3.6 3.6.6.6 0 1 .4 1 1V20c0 .6-.4 1-1 1A17 17 0 0 1 3 4c0-.6.4-1 1-1h3.5c.6 0 1 .4 1 1 0 1.3.2 2.5.6 3.6.1.3 0 .7-.2 1z"/></svg>(248)555-0174</li>
      <li><svg viewBox="0 0 24 24" aria-label="Fax"><path d="M6 2h10v5H6zM3 8h18v9h-3v5H6v-5H3zm5 8v4h8v-4z"/></svg>(248)555-0189</li>
      <li><svg viewBox="0 0 24 24" aria-label="Email"><path d="M12 2a10 10 0 1 0 0 20 10 10 0 0 0 0-20zm-5 6h10l-5 4zm0 2 5 4 5-4v6H7z"/></svg>info@BrightwaveDentalMi.example</li>
    </ul>

    <address class="address">
      <svg viewBox="0 0 30 28" aria-label="Address"><path d="M15 2 1 14h4v12h8v-8h4v8h8V14h4z"/></svg>
      <span>Fennimore Ave. Ste. 8<br>Royal Oak,<br>MI 48059</span>
    </address>
  </section>

  <section class="card card--back" aria-label="Card back">
    <svg class="card__decor" viewBox="0 0 680 390" aria-hidden="true">
      <circle cx="30" cy="60" r="100" fill="var(--circle-a)"/>
      <circle cx="50" cy="150" r="100" fill="var(--circle-b)" opacity="0.8"/>
      <rect x="0" y="230" width="30" height="160" fill="var(--circle-c)" opacity="0.6"/>
    </svg>

    <div class="wordmark">
      <span class="wordmark__dot"></span>
      <span class="wordmark__name">Brightwave Dental Care</span>
    </div>

    <p class="website">BrigthwaveDentalMi.example</p>

    <p class="appointment">( For<span class="blank blank--for"></span> Date <span class="blank blank--date"></span> Time<span class="blank blank--time"></span> )</p>

    <p class="notice">“If you are unable to keep your appointment,<br>kindly give 48 hours notice”</p>
  </section>

</main>
</body>
</html>
```